Verpackungsdesign (Beutel) für Mentholkristalle
Zielgruppe
Wir sind im eCommerce tätig und verkaufen somit ausschließlich online. Zielgruppe für dieses Produkt sind Saunagänger.
Aufgabenstellung
Es handelt sich um ein Design für einen Beutel. Das Produkt sind Mentholkristalle.
Es handelt sich um die Marke KOVAN - wobei dies nicht unbedingt so präsent sein muss. Es gibt kein Logo - es kann allerdings für eine bessere Optik für die Vorderseite ein Logo erstellt werden.
Die Maße des Beutels sind in etwa 130x200mm. Eine Stanzform ist beigefügt.
Dieser Stil gefällt mir gut: https://www.kaufdepot.de/dp/Q527RKMNE9/
Derzeitiges Design: https://www.kaufdepot.de/dp/Q3916P8TLY
Benötigt werden am Ende die Rohdaten (PSD, AI Dateien etc.) sowie sämtlichen Rechte alles kommerziell benutzen sowie verändern zu dürfen.
Ein Briefing ist im Anhang beigefügt.

```html
<!DOCTYPE html>
<html lang="de">
<head>
<meta charset="utf-8">
<title>Mentholkristalle – Beutel Vorderseite</title>
<link rel="stylesheet" href="https://fonts.googleapis.com/css2?family=Open+Sans:wght@500;600&family=Noto+Serif:wght@400;700&family=Yellowtail&display=swap">
<style>
  :root {
    --backdrop: #2bc28a;
    --pouch-green: #25b87c;
    --brush-green: #1fae72;
    --brush-soft: #52c997;
    --paper: #ececea;
    --title-green: #128a5e;
    --ink: #333333;
    --white: #ffffff;
  }
  * { margin: 0; padding: 0; box-sizing: border-box; }
  html, body {
    width: 1200px;
    height: 900px;
    overflow: hidden;
    background: var(--backdrop);
  }
  .canvas {
    position: relative;
    width: 1200px;
    height: 900px;
  }
  .pouch {
    position: absolute;
    left: 405px;
    top: 150px;
    width: 390px;
    height: 600px;
    background: var(--paper);
    overflow: hidden;
  }
  .pouch__brushes {
    position: absolute;
    inset: 0;
    width: 100%;
    height: 100%;
  }
  .pouch__band {
    position: absolute;
    left: 0;
    right: 0;
    bottom: 0;
    height: 172px;
    background: var(--pouch-green);
  }
  .pouch__emblem {
    position: absolute;
    left: 155px;
    top: 128px;
    width: 80px;
    height: 80px;
  }
  .pouch__title {
    position: absolute;
    left: 0;
    right: 0;
    top: 218px;
    text-align: center;
    font-family: "Open Sans", sans-serif;
    font-weight: 500;
    font-size: 34px;
    letter-spacing: 0.2px;
    color: var(--title-green);
  }
  .pouch__claim {
    position: absolute;
    left: 0;
    right: 0;
    top: 274px;
    text-align: center;
    font-family: "Noto Serif", serif;
    font-weight: 700;
    font-size: 13px;
    color: var(--ink);
  }
  .pouch__badge {
    position: absolute;
    left: 300px;
    top: 350px;
    width: 76px;
    height: 78px;
    background: var(--white);
    border-radius: 4px 4px 0 0;
  }
  .pouch__tagline {
    position: absolute;
    left: 0;
    right: 0;
    top: 490px;
    text-align: center;
    font-family: "Yellowtail", cursive;
    font-size: 27px;
    color: var(--white);
  }
  .pouch__weight {
    position: absolute;
    right: 40px;
    top: 546px;
    font-family: "Noto Serif", serif;
    font-size: 16px;
    color: var(--white);
  }
</style>
</head>
<body>
  <main class="canvas">
    <section class="pouch" aria-label="Beutel Mentholkristalle">
      <svg class="pouch__brushes" viewBox="0 0 390 600" role="img" aria-label="Grüne Pinselstriche als Hintergrundgestaltung">
        <path d="M130 0 H390 V110 C330 100 260 120 205 105 C160 92 135 60 130 0 Z" fill="var(--brush-green)"/>
        <path d="M0 0 H40 L60 40 C40 120 50 220 40 300 L20 290 C10 200 15 100 0 40 Z" fill="var(--brush-soft)"/>
        <path d="M390 190 C340 220 290 250 250 300 C210 350 170 400 130 430 L260 430 C300 390 340 330 390 290 Z" fill="var(--brush-soft)"/>
        <path d="M110 310 H330 V430 H110 Z" fill="var(--brush-green)" opacity="0.85"/>
        <path d="M0 330 C40 325 80 340 120 335 L118 345 C80 350 40 340 0 345 Z" fill="var(--brush-soft)"/>
      </svg>
      <div class="pouch__band"></div>
      <svg class="pouch__emblem" viewBox="0 0 80 80" role="img" aria-label="Illustration Minzblätter">
        <circle cx="40" cy="40" r="36" fill="var(--brush-green)"/>
      </svg>
      <h1 class="pouch__title">Mentholkristalle</h1>
      <p class="pouch__claim">100% natürlich</p>
      <div class="pouch__badge" aria-label="Recycling-Siegel"></div>
      <p class="pouch__tagline">„Ideal für die Sauna“</p>
      <p class="pouch__weight">100g</p>
    </section>
  </main>
</body>
</html>
```